Dental Veloria Postcard Mailer

We need a two sided, professional looking postcard to send to dentists that will explain our business. Dental Veloria offers to buy the buildings that dentists own and then lease it back to them until they are ready to retire. This will free up their capital while allowing them to continue to work before retirement. Excellent for those needing liquidity or pre-retirement prep. PLEASE FEEL FREE TO IMPROVE COPY POINTS AND EVEN MAKE THE LOGO MORE PROFESSIONAL LOOKING

Target Market(s)

DENTISTS AND MEDICAL PROFESSIONALS

Industry/Entity Type

Business

Font styles to use
Serif
Sans Serif

Requirements
Must have
• OUR LOGO, PHONE NUMBER. COPY POINTS EXPLAINING OUR BUSINESS. PLACE FOR MAILING ADDRESS, FOLLOW STANDARD KRVB GUIDELINES
Nice to have
• screen background of inside of dentist office or something indicating the freeing up of money...very professional looking. ok to tweak the logo to look a little more professional.

```html
<!DOCTYPE html>
<html lang="en">
<head>
<meta charset="utf-8">
<title>Dental Veloria Postcard Mailer</title>
<link rel="stylesheet" href="https://fonts.googleapis.com/css2?family=Source+Sans+3:wght@400;600;700&display=swap">
<style>
:root{
  --navy:#14357a;
  --navy-deep:#0e2a66;
  --blue:#0a6fbf;
  --blue-mid:#1666b4;
  --tab:#1b4f9c;
  --silver:#c9cbcf;
  --silver-light:#f4f4f4;
  --ink:#5b5f66;
  --white:#ffffff;
  --line:#b9bcc0;
  --page:#e9eaec;
}
*{box-sizing:border-box;margin:0;padding:0}
html,body{width:1078px;height:1200px;overflow:hidden;background:var(--page);font-family:"Source Sans 3",Arial,sans-serif}
.canvas{position:relative;width:1078px;height:1200px}
.card{position:absolute;width:863px;height:558px;background:var(--white);overflow:hidden;box-shadow:0 2px 8px rgba(0,0,0,.18)}
.card--front{left:40px;top:12px}
.card--back{left:175px;top:624px}
.card__art{position:absolute;inset:0}
.abs{position:absolute}

/* front */
.front__kicker{left:33px;top:54px;color:var(--white);font-size:19px;letter-spacing:.2px}
.wordmark{display:flex;align-items:center;gap:14px;color:var(--navy);font-weight:600;white-space:nowrap}
.wordmark__dot{border-radius:50%;background:var(--navy);flex:none}
.front__brand{left:362px;top:50px;font-size:36px}
.front__brand .wordmark__dot{width:46px;height:46px}
.front__intro{left:388px;top:160px;width:460px;color:var(--ink);font-size:17.5px;line-height:18px}
.front__intro b{color:var(--navy);font-weight:400}
.tab{display:flex;align-items:center;color:var(--white);font-weight:600;background:linear-gradient(90deg,var(--blue-mid),var(--tab));box-shadow:3px 4px 6px rgba(0,0,0,.3)}
.front__tab{left:400px;top:245px;width:320px;height:57px;padding-left:25px;font-size:21px;border-radius:0 28px 28px 0}
.ticks{list-style:none;color:var(--white)}
.ticks li{position:relative;padding-left:24px}
.ticks svg{position:absolute;left:0;top:3px}
.front__ticks{left:424px;top:322px;width:420px;font-size:16px;line-height:21px}
.front__ticks li{margin-bottom:20px}
.front__note{left:449px;top:466px;color:var(--white);font-size:10px;line-height:13px}
.tollfree{display:flex;align-items:center;gap:8px;font-weight:700;white-space:nowrap}
.tollfree__label{font-size:21px}
.tollfree__num{font-size:25px;letter-spacing:.5px}
.front__call{right:22px;top:516px;color:var(--white)}

/* back */
.back__brand{left:26px;top:122px;font-size:20px}
.back__brand .wordmark__dot{width:22px;height:22px}
.back__tab{left:0;top:201px;width:218px;height:44px;padding-left:25px;font-size:23px;border-radius:0 22px 22px 0}
.back__ticks{left:28px;top:265px;width:440px;font-size:14.5px;line-height:17px}
.back__ticks li{margin-bottom:8px}
.back__contact{left:0;top:423px;width:470px;height:64px;text-align:center;color:var(--navy)}
.back__contact-lead{display:block;padding-top:7px;font-size:11.5px;color:#2b2f36}
.back__contact .tollfree{justify-content:center;margin-top:4px}
.back__email{left:0;top:502px;width:470px;text-align:center;color:var(--white);font-size:19px;font-weight:600;display:flex;justify-content:center;align-items:center;gap:7px}
</style>
</head>
<body>
<div class="canvas">

  <!-- FRONT -->
  <section class="card card--front">
    <svg class="card__art" width="863" height="558" viewBox="0 0 863 558">
      <defs>
        <linearGradient id="silverHead" x1="0" x2="1">
          <stop offset="0" stop-color="#ffffff"/><stop offset=".6" stop-color="#f1f1f2"/><stop offset="1" stop-color="#b9bbbf"/>
        </linearGradient>
        <linearGradient id="kickerBand" x1="0" x2="1">
          <stop offset="0" stop-color="#1b4f9c"/><stop offset="1" stop-color="#0a6fbf"/>
        </linearGradient>
        <linearGradient id="photoTone" x1="0" x2="1" y1="0" y2="1">
          <stop offset="0" stop-color="#e6ebef"/><stop offset=".5" stop-color="#8fa9cf"/><stop offset="1" stop-color="#3d4f79"/>
        </linearGradient>
        <linearGradient id="navyBar" x1="0" x2="1">
          <stop offset="0" stop-color="#0e2a66"/><stop offset="1" stop-color="#14357a"/>
        </linearGradient>
      </defs>
      <rect width="863" height="558" fill="#f3f3f4"/>
      <rect x="0" y="0" width="863" height="128" fill="url(#silverHead)"/>
      <polygon points="0,0 252,0 325,128 0,128" fill="url(#kickerBand)"/>
      <rect x="0" y="127" width="863" height="5" fill="var(--navy)"/>
      <rect x="380" y="270" width="483" height="230" fill="var(--blue)"/>
      <rect x="300" y="510" width="563" height="48" fill="url(#navyBar)"/>
      <ellipse cx="130" cy="400" rx="282" ry="308" fill="var(--blue-mid)"/>
      <ellipse cx="130" cy="400" rx="274" ry="300" fill="#ffffff"/>
      <ellipse cx="130" cy="400" rx="270" ry="295" fill="url(#photoTone)" role="img" aria-label="Photo: smiling dentist in blue scrubs, arms crossed, in a treatment room"/>
      <rect x="0" y="132" width="863" height="0" fill="none"/>
    </svg>
    <p class="abs front__kicker">NEED WORKING CAPITAL?</p>
    <div class="abs wordmark front__brand"><span class="wordmark__dot"></span>DENTAL VELORIA, LLC</div>
    <p class="abs front__intro"><b>Dental Veloria, LLC</b> has developed and refined a system that offers financial services to the dental profession.</p>
    <h2 class="abs tab front__tab">HOW THE PROGRAM WORKS</h2>
    <ul class="abs ticks front__ticks">
      <li><svg width="16" height="16" viewBox="0 0 16 16"><rect x="1" y="2" width="12" height="12" rx="2" fill="none" stroke="#fff" stroke-width="1.6"/><path d="M4 8l3 3 7-8" fill="none" stroke="#fff" stroke-width="1.8"/></svg>Sell your real estate to Dental Veloria now</li>
      <li><svg width="16" height="16" viewBox="0 0 16 16"><rect x="1" y="2" width="12" height="12" rx="2" fill="none" stroke="#fff" stroke-width="1.6"/><path d="M4 8l3 3 7-8" fill="none" stroke="#fff" stroke-width="1.8"/></svg>Occupy it as before under a lease from Dental Veloria</li>
      <li><svg width="16" height="16" viewBox="0 0 16 16"><rect x="1" y="2" width="12" height="12" rx="2" fill="none" stroke="#fff" stroke-width="1.6"/><path d="M4 8l3 3 7-8" fill="none" stroke="#fff" stroke-width="1.8"/></svg>Retire or sell your practice when you are ready without the hassle of dealing with the real estate</li>
    </ul>
    <p class="abs front__note">Properties will be assessed for qualification to the program on an individual basis.<br>All terms are negotiated</p>
    <div class="abs tollfree front__call">
      <span class="tollfree__label">Toll Free</span>
      <svg width="20" height="20" viewBox="0 0 24 24"><path d="M6.6 10.8a15 15 0 006.6 6.6l2.2-2.2a1 1 0 011-.25 11.4 11.4 0 003.6.6 1 1 0 011 1V20a1 1 0 01-1 1A17 17 0 013 4a1 1 0 011-1h3.5a1 1 0 011 1c0 1.25.2 2.45.6 3.6a1 1 0 01-.25 1z" fill="#fff"/></svg>
      <span class="tollfree__num">844-555-0187</span>
    </div>
  </section>

  <!-- BACK -->
  <section class="card card--back">
    <svg class="card__art" width="863" height="558" viewBox="0 0 863 558">
      <defs>
        <linearGradient id="logoPanel" x1="0" x2="1">
          <stop offset="0" stop-color="#ffffff"/><stop offset="1" stop-color="#d9dadc"/>
        </linearGradient>
        <linearGradient id="roomTone" x1="0" x2="1" y1="0" y2="1">
          <stop offset="0" stop-color="#f2f5f6"/><stop offset=".55" stop-color="#b8dbe3"/><stop offset="1" stop-color="#3fa3c2"/>
        </linearGradient>
        <linearGradient id="contactBar" x1="0" x2="1">
          <stop offset="0" stop-color="#ffffff"/><stop offset=".6" stop-color="#f0f0f0"/><stop offset="1" stop-color="#bfc1c4"/>
        </linearGradient>
        <linearGradient id="footBar" x1="0" x2="1">
          <stop offset="0" stop-color="#1f3a94"/><stop offset="1" stop-color="#0e2a66"/>
        </linearGradient>
      </defs>
      <rect width="470" height="173" fill="url(#logoPanel)"/>
      <rect x="275" y="0" width="195" height="173" fill="url(#roomTone)" role="img" aria-label="Photo: bright modern dental treatment room with patient chair"/>
      <rect x="0" y="173" width="470" height="250" fill="var(--blue)"/>
      <rect x="0" y="423" width="470" height="64" fill="url(#contactBar)"/>
      <rect x="0" y="487" width="470" height="71" fill="url(#footBar)"/>
      <rect x="742.5" y="20.5" width="102" height="73" fill="#fff" stroke="var(--line)"/>
      <g stroke="var(--line)" stroke-width="1.2">
        <line x1="530" y1="228" x2="844" y2="228"/>
        <line x1="530" y1="265" x2="844" y2="265"/>
        <line x1="530" y1="301" x2="844" y2="301"/>
        <line x1="530" y1="338" x2="844" y2="338"/>
        <line x1="530" y1="375" x2="844" y2="375"/>
      </g>
    </svg>
    <div class="abs wordmark back__brand"><span class="wordmark__dot"></span>DENTAL VELORIA, LLC</div>
    <h2 class="abs tab back__tab">WHO BENEFITS?</h2>
    <ul class="abs ticks back__ticks">
      <li><svg width="14" height="14" viewBox="0 0 16 16"><rect x="1" y="2" width="12" height="12" rx="2" fill="none" stroke="#fff" stroke-width="1.6"/><path d="M4 8l3 3 7-8" fill="none" stroke="#fff" stroke-width="1.8"/></svg>Any dental professional wanting to use building equity to invest in an existing practice.</li>
      <li><svg width="14" height="14" viewBox="0 0 16 16"><rect x="1" y="2" width="12" height="12" rx="2" fill="none" stroke="#fff" stroke-width="1.6"/><path d="M4 8l3 3 7-8" fill="none" stroke="#fff" stroke-width="1.8"/></svg>Any dental professional wanting to be free of building ownership responsibilities.</li>
      <li><svg width="14" height="14" viewBox="0 0 16 16"><rect x="1" y="2" width="12" height="12" rx="2" fill="none" stroke="#fff" stroke-width="1.6"/><path d="M4 8l3 3 7-8" fill="none" stroke="#fff" stroke-width="1.8"/></svg>Any dental professional wanting to pre-plan for retirement with a solid exit strategy while freeing up cash for other uses now.</li>
    </ul>
    <div class="abs back__contact">
      <span class="back__contact-lead">Contact us today for a free, no obligation consultation:</span>
      <div class="tollfree">
        <span class="tollfree__label">Toll Free</span>
        <svg width="20" height="20" viewBox="0 0 24 24"><path d="M6.6 10.8a15 15 0 006.6 6.6l2.2-2.2a1 1 0 011-.25 11.4 11.4 0 003.6.6 1 1 0 011 1V20a1 1 0 01-1 1A17 17 0 013 4a1 1 0 011-1h3.5a1 1 0 011 1c0 1.25.2 2.45.6 3.6a1 1 0 01-.25 1z" fill="var(--navy)"/></svg>
        <span class="tollfree__num">844-555-0187</span>
      </div>
    </div>
    <p class="abs back__email">
      <svg width="15" height="15" viewBox="0 0 16 16"><circle cx="8" cy="8" r="7.5" fill="#fff"/><rect x="4" y="5" width="8" height="6" fill="none" stroke="var(--navy)" stroke-width="1.2"/><path d="M4 5l4 3.5L12 5" fill="none" stroke="var(--navy)" stroke-width="1.2"/></svg>
      info@dentalveloriallc.com
    </p>
  </section>

</div>
</body>
</html>
```